Company Brochure promoting our Managed Services Business (MSP)

Objective: Is the brochure meant to generate leads, educate potential clients, and promote our Managed Services Business.
Target Audience: is for Small to medium size business.
A managed service provider like Brivanta Advisory Group handles a variety of different responsibilities for Business
. We oversee vital IT resources such as:
Email
Cloud integration
Data storage
Networking
Cybersecurity
File backup
Help desk services
Our firm also provides remote monitoring services and updates. As part of our managed service provider solutions, we will continually report on the performance and quality of your network. We can even help your organization acquire new hardware and software.
At Brivanta Advisory Group we specialize in empowering commercial businesses with robust IT solutions tailored to enhance efficiency, security, and scalability. With years of expertise in Managed Services, we understand the unique challenges businesses face in today’s digital landscape.
Call-to-Action (CTA):
Encourage readers to contact you, visit your website, or schedule a consultation.
you can get an overview of BAG at www..brivantaag.com.
Layout: Opt for a clean, easy-to-read layout with well-defined sections.
Imagery:
Include professional photos, custom graphics, or icons that represent your services.
Avoid generic stock images when possible.
Format: Tri-fold, bi-fold, depending on the amount of information.
We would like to have a section of the "q7" from our web site.
I have attached the Logos.
Target Market(s)
Small to Medium Business
Look and feel

```html
<!DOCTYPE html>
<html lang="en">
<head>
<meta charset="utf-8">
<title>Brivanta Advisory Group – Managed Services Tri-fold</title>
<link rel="stylesheet" href="https://fonts.googleapis.com/css2?family=Krona+One&family=Poppins:ital,wght@0,400;0,500;0,600;0,700;1,400;1,600&display=swap">
<style>
:root{
  --teal:#1a6e84;
  --teal-dark:#124c5d;
  --teal-deep:#0e3d4b;
  --teal-bright:#1f8fab;
  --ink:#1c5466;
  --paper:#ffffff;
  --backdrop:#e6e6e6;
}
*{box-sizing:border-box;margin:0;padding:0}
html,body{width:1200px;height:2448px;overflow:hidden}
body{background:var(--backdrop);font-family:"Poppins",sans-serif;color:var(--ink);position:relative}
.spread{position:absolute;left:30px;width:1140px;height:806px;background:var(--paper);box-shadow:0 6px 24px rgba(0,0,0,.18);overflow:hidden}
.spread--outer{top:318px}
.spread--inner{top:1324px}
.panel{position:absolute;top:0;width:380px;height:806px;overflow:hidden}
.panel--1{left:0}.panel--2{left:380px}.panel--3{left:760px}
.heading{font-family:"Krona One",sans-serif;text-transform:uppercase;letter-spacing:.5px;line-height:1.15}
.photo{position:absolute}
svg{display:block}

/* name mark: plain circle + name in text font */
.name-mark{position:absolute;display:flex;align-items:center;gap:14px}
.name-mark .dot-plain{flex:none;border-radius:50%;background:var(--teal)}
.name-mark .name{font-family:"Poppins",sans-serif;font-weight:600;color:var(--teal)}

/* outer: back panel */
.back{background:var(--teal-dark);color:#fff}
.back .heading{font-size:17px;position:absolute;left:34px}
.back .about-title{top:40px}
.back .about-text{position:absolute;left:34px;top:72px;width:310px;font-size:11.5px;line-height:1.55;font-style:italic}
.back .offer-title{top:232px}
.offer-list{position:absolute;left:0;top:272px;width:360px;list-style:none}
.offer-list li{position:relative;height:44px;margin-bottom:12px}
.offer-list .bar{position:absolute;left:60px;top:8px;right:0;height:28px;background:linear-gradient(90deg,var(--teal-bright),var(--teal));clip-path:polygon(0 0,100% 0,94% 100%,0 100%)}
.offer-list .dot{position:absolute;left:34px;top:4px;width:36px;height:36px;border-radius:50%;background:#fff;border:3px solid var(--teal-bright);display:flex;align-items:center;justify-content:center}
.offer-list .label{position:absolute;left:84px;top:13px;font-size:11px;font-weight:600;font-style:italic}
.back .cta-photo{left:0;top:560px;width:380px;height:130px;background:linear-gradient(120deg,#0d3a48,#2a9fbd 55%,#0f4656)}
.back .cta{position:absolute;left:0;top:690px;width:380px;height:116px;background:var(--teal);padding:28px 34px}
.back .cta .heading{position:static;font-size:20px;line-height:1.3}

/* outer: middle panel */
.contact{background:var(--paper)}
.contact .tri-photo{left:0;top:0;width:380px;height:400px}
.contact .name-mark{left:110px;top:100px}
.contact .dot-plain{width:64px;height:64px}
.contact .name{font-size:34px}
.contact-list{position:absolute;left:40px;top:430px;list-style:none}
.contact-list li{display:flex;gap:14px;margin-bottom:18px}
.contact-list .ico{width:26px;height:26px;border-radius:50%;background:var(--teal);flex:none;display:flex;align-items:center;justify-content:center}
.contact-list small{display:block;font-size:11px;color:var(--ink)}
.contact-list strong{display:block;font-size:14px;font-weight:600;line-height:1.3;color:var(--teal-deep)}

/* outer: cover */
.cover{background:var(--paper)}
.cover .hero{left:0;top:0;width:380px;height:420px}
.cover .headline{position:absolute;left:34px;top:440px;font-size:27px;color:var(--teal);line-height:1.2}
.cover .band{position:absolute;left:0;top:640px;width:380px;height:166px;background:var(--teal)}
.cover .name-mark{left:34px;top:690px}
.cover .dot-plain{width:70px;height:70px;border-radius:0;background:#fff}
.cover .name{color:#fff;font-weight:500;font-size:19px;line-height:1.25;text-transform:uppercase;letter-spacing:1px}

/* inner: panel 1 */
.mission .heading{position:absolute;left:44px;top:44px;font-size:19px;color:var(--teal-deep)}
.mission .lead{position:absolute;left:44px;top:88px;width:310px;font-size:13.4px;line-height:1.42;text-align:justify;color:var(--teal-deep)}
.services{position:absolute;left:0;top:330px;width:380px;height:476px;background:var(--teal-dark)}
.services .photo{right:0;top:-60px;width:200px;height:220px;clip-path:polygon(100% 0,100% 100%,0 100%,35% 15%);background:linear-gradient(160deg,#8fe0f2,#2da6c3 45%,#0f5466)}
.services .heading{position:absolute;left:44px;top:22px;font-size:19px;color:#fff}
.service-list{position:absolute;left:0;top:100px;width:380px;list-style:none}
.service-list li{position:relative;height:50px;margin-bottom:20px;background:linear-gradient(90deg,var(--teal),var(--teal-bright))}
.service-list .tab{position:absolute;left:0;top:0;width:110px;height:50px;background:#fff;clip-path:polygon(0 0,78% 0,100% 100%,0 100%);display:flex;align-items:center;padding-left:44px}
.service-list .label{position:absolute;left:112px;top:15px;font-size:13px;font-weight:600;color:#fff}

/* inner: panel 2 */
.method .photo{left:0;top:0;width:380px;height:270px;background:radial-gradient(circle at 70% 30%,#f2f2f2,#bdbdbd 45%,#6f6f6f);clip-path:polygon(0 0,100% 0,100% 210px,0 270px)}
.method .name-mark{left:240px;top:130px}
.method .dot-plain{width:46px;height:46px}
.method .name{font-size:26px;color:#fff}
.method .heading{position:absolute;left:20px;top:284px;font-size:18px;color:var(--teal)}
.method .intro{position:absolute;left:20px;top:342px;width:320px;font-size:12.6px;line-height:1.48;color:var(--teal-deep)}
.method .intro b{font-weight:700}
.tag{display:inline-block;background:var(--teal-bright);color:#fff;font-size:12.5px;font-weight:600;padding:3px 18px 3px 12px;clip-path:polygon(0 0,88% 0,100% 50%,88% 100%,0 100%,6% 50%)}
.bullets{list-style:none;margin:12px 0 0}
.bullets li{position:relative;padding-left:16px;font-size:12.6px;line-height:1.35;margin-bottom:7px;color:var(--teal-deep);text-align:justify}
.bullets li::before{content:"";position:absolute;left:0;top:7px;width:5px;height:5px;border-radius:50%;background:var(--teal)}
.method .steps{position:absolute;left:20px;top:516px;width:320px}
.method .steps .bullets{margin-bottom:14px}

/* inner: panel 3 */
.steps-cont{position:absolute;left:20px;top:40px;width:330px}
.steps-cont p{font-size:12.6px;line-height:1.35;color:var(--teal-deep);margin-bottom:7px;text-align:justify}
.steps-cont .tag{margin-top:16px}
.steps-cont .bullets{margin-bottom:12px}
</style>
</head>
<body>

<section class="spread spread--outer">

  <div class="panel panel--1 back">
    <h2 class="heading about-title">About Us</h2>
    <p class="about-text">Brivanta Advisory Group empowers businesses of all sizes to thrive in the digital age by leveraging our extensive experience, deep industry knowledge and advanced technological solutions. We are committed to delivering superior results and fostering long-term partnerships with our clients, helping them achieve their goals and stay ahead of the competition.</p>
    <h2 class="heading offer-title">What We Offer</h2>
    <ul class="offer-list">
      <li><span class="bar"></span><span class="dot"><svg width="16" height="16" viewBox="0 0 16 16"><rect x="1" y="1" width="5" height="5" fill="#1f8fab"/><rect x="10" y="10" width="5" height="5" fill="#1f8fab"/><circle cx="12.5" cy="3.5" r="2.5" fill="#1f8fab"/><circle cx="3.5" cy="12.5" r="2.5" fill="#1f8fab"/></svg></span><span class="label">Workflow Management</span></li>
      <li><span class="bar"></span><span class="dot"><svg width="16" height="16" viewBox="0 0 16 16"><rect x="3" y="1" width="10" height="14" rx="1" fill="none" stroke="#1f8fab" stroke-width="2"/><path d="M6 5h4M6 8h4M6 11h4" stroke="#1f8fab" stroke-width="1.5"/></svg></span><span class="label">Account Management Services</span></li>
      <li><span class="bar"></span><span class="dot"><svg width="16" height="16" viewBox="0 0 16 16"><circle cx="8" cy="8" r="5" fill="none" stroke="#1f8fab" stroke-width="2"/><circle cx="8" cy="8" r="2" fill="#1f8fab"/></svg></span><span class="label">Business Technologies</span></li>
      <li><span class="bar"></span><span class="dot"><svg width="16" height="16" viewBox="0 0 16 16"><rect x="1" y="3" width="14" height="9" rx="1" fill="none" stroke="#1f8fab" stroke-width="2"/><path d="M4 14h8" stroke="#1f8fab" stroke-width="2"/></svg></span><span class="label">Training &amp; Education Services</span></li>
      <li><span class="bar"></span><span class="dot"><svg width="16" height="16" viewBox="0 0 16 16"><path d="M2 6h9M5 10h9" stroke="#1f8fab" stroke-width="2.5" stroke-linecap="round"/></svg></span><span class="label">And Much More!</span></li>
    </ul>
    <div class="photo cta-photo" role="img" aria-label="Photo of a businessman standing before a glowing blue digital city skyline"></div>
    <div class="cta"><h2 class="heading">Looking to<br>get started?</h2></div>
  </div>

  <div class="panel panel--2 contact">
    <svg class="photo tri-photo" viewBox="0 0 380 400" role="img" aria-label="Collage of data centre and code screens in blue tones">
      <defs><linearGradient id="techBlue" x1="0" y1="0" x2="1" y2="1"><stop offset="0" stop-color="#0e3d4b"/><stop offset=".5" stop-color="#2a9fbd"/><stop offset="1" stop-color="#124c5d"/></linearGradient></defs>
      <polygon points="0,130 130,250 0,380" fill="url(#techBlue)"/>
      <polygon points="380,0 380,330 230,300 260,190" fill="url(#techBlue)"/>
    </svg>
    <div class="name-mark"><span class="dot-plain"></span><span class="name">q7</span></div>
    <ul class="contact-list">
      <li><span class="ico"><svg width="13" height="13" viewBox="0 0 16 16"><path d="M3 1l3 3-2 2c1 2 3 4 6 6l2-2 3 3-2 3C7 16 0 9 0 3z" fill="#fff"/></svg></span><div><small>Call Us:</small><strong>1-855-BRIVAAG</strong></div></li>
      <li><span class="ico"><svg width="13" height="13" viewBox="0 0 16 16"><rect x="1" y="3" width="14" height="10" rx="1" fill="#fff"/><path d="M1 4l7 5 7-5" stroke="#1a6e84" stroke-width="1.5" fill="none"/></svg></span><div><small>Mail Us:</small><strong>sales@brivantaag.com</strong></div></li>
      <li><span class="ico"><svg width="13" height="13" viewBox="0 0 16 16"><circle cx="8" cy="8" r="6.5" fill="none" stroke="#fff" stroke-width="1.5"/><path d="M1.5 8h13M8 1.5c3 3 3 10 0 13M8 1.5c-3 3-3 10 0 13" stroke="#fff" stroke-width="1.2" fill="none"/></svg></span><div><small>Website:</small><strong>www.brivantaag.com</strong></div></li>
      <li><span class="ico"><svg width="13" height="13" viewBox="0 0 16 16"><path d="M8 15s-5-5-5-9a5 5 0 0110 0c0 4-5 9-5 9z" fill="#fff"/><circle cx="8" cy="6" r="2" fill="#1a6e84"/></svg></span><div><small>HQ Address:</small><strong>820 Harbor View Lane<br>Suite 210<br>Coral Bay, FL 32190</strong></div></li>
    </ul>
  </div>

  <div class="panel panel--3 cover">
    <svg class="photo hero" viewBox="0 0 380 420" role="img" aria-label="Greyscale photo of a robotic hand reaching toward a glowing digital network sphere">
      <defs><radialGradient id="heroGrey" cx=".55" cy=".45" r=".7"><stop offset="0" stop-color="#f4f4f4"/><stop offset=".6" stop-color="#bdbdbd"/><stop offset="1" stop-color="#7d7d7d"/></radialGradient></defs>
      <rect width="380" height="420" fill="url(#heroGrey)"/>
      <polygon points="380,290 380,420 200,420" fill="#1a6e84"/>
    </svg>
    <h1 class="heading headline">Providing<br>Innovative<br>Technology<br>Solutions</h1>
    <div class="band"></div>
    <div class="name-mark"><span class="dot-plain"></span><span class="name">Brivanta<br>Advisory<br>Group</span></div>
  </div>
</section>

<section class="spread spread--inner">

  <div class="panel panel--1 mission">
    <h2 class="heading">Mission &amp; Vission</h2>
    <p class="lead"><b>Brivanta Advisory</b> Group empowers your business to thrive in the digital age. Our team of expert consultants specializes in transforming your technology landscape – streamlining operations, enhancing security, and driving innovation. Whether you're looking to implement cutting-edge solutions or optimize existing systems, we tailor our approach to meet your unique needs, ensuring you stay ahead of the competition and achieve your strategic goals.</p>
    <div class="services">
      <div class="photo" role="img" aria-label="Photo of engineers in hard hats reviewing plans in a bright blue-lit factory"></div>
      <h2 class="heading">Our<br>Services</h2>
      <ul class="service-list">
        <li><span class="tab"><svg width="26" height="26" viewBox="0 0 26 26"><circle cx="13" cy="11" r="7" fill="none" stroke="#1f8fab" stroke-width="3" stroke-dasharray="4 2"/><circle cx="13" cy="11" r="2.5" fill="#1f8fab"/><path d="M3 22c3-3 7-3 10 0s7 3 10 0" stroke="#1f8fab" stroke-width="2" fill="none"/></svg></span><span class="label">Managed Services</span></li>
        <li><span class="tab"><svg width="26" height="26" viewBox="0 0 26 26"><rect x="2" y="2" width="8" height="8" fill="#1f8fab"/><rect x="16" y="16" width="8" height="8" fill="#1f8fab"/><circle cx="20" cy="6" r="4" fill="#1f8fab"/><circle cx="6" cy="20" r="4" fill="#1f8fab"/></svg></span><span class="label">Workflow Management</span></li>
        <li><span class="tab"><svg width="26" height="26" viewBox="0 0 26 26"><rect x="4" y="2" width="14" height="20" rx="1" fill="none" stroke="#1f8fab" stroke-width="2"/><rect x="12" y="12" width="3" height="12" fill="#1f8fab"/><rect x="17" y="8" width="3" height="16" fill="#1f8fab"/><rect x="22" y="15" width="3" height="9" fill="#1f8fab"/></svg></span><span class="label">Account Management Services</span></li>
        <li><span class="tab"><svg width="28" height="26" viewBox="0 0 28 26"><path d="M2 8l8-2 5 4 5-4 6 2v10l-6 2-5-4-5 4-8-2z" fill="#1f8fab"/></svg></span><span class="label">Business Technologies</span></li>
        <li><span class="tab"><svg width="26" height="26" viewBox="0 0 26 26"><path d="M4 7l9-4 9 4-9 4z" fill="#1f8fab"/><rect x="3" y="12" width="20" height="10" rx="1" fill="none" stroke="#1f8fab" stroke-width="2"/></svg></span><span class="label">Training &amp; Education Services</span></li>
      </ul>
    </div>
  </div>

  <div class="panel panel--2 method">
    <div class="photo" role="img" aria-label="Greyscale photo of a woman interacting with floating holographic data screens"></div>
    <div class="name-mark"><span class="dot-plain"></span><span class="name">q7</span></div>
    <h2 class="heading">Q7 Exponential<br>Results</h2>
    <p class="intro">Brivanta Advisory Group believes every successful technology initiative requires a structured, results-driven approach. Our 5 E's methodology <b>Evaluate, Enhance, Engineer, Execute, and Evolve</b> is designed to ensure each project not only meets your immediate needs but also positions your organization for long-term success.</p>
    <div class="steps">
      <span class="tag">Evaluate</span>
      <ul class="bullets">
        <li>Review a client's current infrastructure and procedures as they relate to stated goals.</li>
        <li>Introduce tools for evaluation, such as performance metrics, feedback mechanisms, or audits.</li>
        <li>Stress the value of involving all stakeholders to get a comprehensive understanding of the workflow's strengths and weaknesses.</li>
      </ul>
      <span class="tag">Enhance</span>
    </div>
  </div>

  <div class="panel panel--3">
    <div class="steps-cont">
      <p>Identify opportunities for improvement. Focus on necessary adjustments to streamline inefficiencies and/or adopt best practices.</p>
      <p>Demonstrate how the solution achieves goals identified in Evaluate step.</p>
      <p>Real-World Insights: We've walked the walk. Years of experience and practical knowledge distilled into actionable strategies you can implement right away.</p>
      <span class="tag">Engineer</span>
      <ul class="bullets">
        <li>Design the solution and structure the process of implementation.</li>
        <li>Ensure that workflow and timeframe KPI's are clearly delineated and that tools and technologies are aligned.</li>
        <li>Formalize changes and change procedures.</li>
      </ul>
      <span class="tag">Execute</span>
      <ul class="bullets">
        <li>Put the plan into action. Project management is key. Adhere to timeframes and KPI's.</li>
        <li>Communicate clearly as stages are completed w/ key stakeholder signoff.</li>
        <li>Communicate clearly if change orders are required/ requested with key stakeholder signoff.</li>
      </ul>
      <span class="tag">Evolve</span>
      <ul class="bullets">
        <li>Quarterly Business Reviews.</li>
        <li>Embrace a mindset of constant growth, adaptability and innovation.</li>
        <li>Look to improve existing Brivanta solutions and discover untapped potential.</li>
        <li>If we weren't already doing it this way, which way would we start?</li>
      </ul>
    </div>
  </div>
</section>

</body>
</html>
```